Varden Institute for Restorative Care

I need a full informational website for my medical practice. I would like to use my logo and also include a lot of emblems/pictures (also a picture of me in a white coat). The website should have a function for people to inquire and send me messages. I will be offering needle-less regenerative injection therapy, stem cell treatments, bioidentical hormone therapy, treatment for chronic illness, neurodegenerative diseases, skin rejuvenation, hair restoration, male enhancement, female enhancement, and anti-aging. The practice will not be accepting insurance and will be cash/credit card only.
A good example of written content and functionality is this website:
http://thebrvx.example/. However, I want different theme and tones.
Target Market(s)
High end clientele in Los Angeles, Southern California. Health minded people who are interested in living better and longer and can afford anti-aging treatments. Men and women who want to improve sexual health and wellbeing.
Requirements
Must have
- 1. I will need to be able to move the site to other servers (needed for site speed)
- 2. Site must be build on WordPress
- 3. Full admin credentials for domain, cpanel, wordpress, ftp.
- 4. No third party interaction on development and content deployment once the site is on different servers
- 5. I will need the ability to add content and links to the site
- 6. I will need the ability to optimize the site for speed
- 7. I will need to ability to modify URLs so they are more SEO friendly
Nice to have
- pictures of stem cells, health improvement and regeneration, beauty, youthful individuals, older healthy and happy individuals. Medical designs.
Should not have
- flowers, dna

```html
<!DOCTYPE html>
<html lang="en">
<head>
<meta charset="utf-8">
<title>Varden Institute for Restorative Care</title>
<link href="https://fonts.googleapis.com/css2?family=Cinzel:wght@400;700&family=Lato:ital,wght@0,400;0,700;1,400&family=Open+Sans:wght@300;600&display=swap" rel="stylesheet">
<style>
:root{
  --green:#1fa27f;
  --green-dark:#178a6b;
  --green-soft:#7fcfbd;
  --navy:#0f1c6e;
  --ink:#2b2b2b;
  --grey:#6f6f6f;
  --white:#ffffff;
  --hero-a:#1d5a74;
  --hero-b:#5fa3bd;
  --map:#e7e9e6;
}
*{box-sizing:border-box;margin:0;padding:0}
html,body{width:1200px;height:3429px;overflow:hidden}
body{font-family:"Lato",sans-serif;color:var(--ink);background:var(--white);position:relative}
section,header,footer{position:absolute;left:0;width:1200px}
.abs{position:absolute}

/* header */
.site-header{top:0;height:135px;background:var(--white)}
.topbar{right:0;top:0;width:430px;height:41px;background:var(--green);color:var(--white);font-size:15px;display:flex;align-items:center;justify-content:flex-end;gap:34px;padding-right:80px}
.topbar span{display:flex;align-items:center;gap:10px}
.brand{left:78px;top:18px;display:flex;align-items:center;gap:14px}
.brand-dot{width:44px;height:44px;border-radius:50%;background:var(--navy);flex:none}
.brand-name{font-family:"Cinzel",serif;font-weight:700;color:var(--navy);font-size:19px;line-height:1.2;width:240px}
.main-nav{right:78px;top:78px;display:flex;gap:30px;font-size:15px;color:var(--ink);letter-spacing:.3px;align-items:center}
.main-nav .active{color:var(--green);position:relative}
.main-nav .active::after{content:"";position:absolute;left:-8px;right:-8px;top:44px;height:4px;background:var(--green)}

/* hero */
.hero{top:135px;height:542px;background:radial-gradient(circle at 35% 50%,#4f8fa9 0,var(--hero-a) 70%)}
.hero-photo{left:0;top:0;width:1200px;height:542px;background:
  radial-gradient(circle at 390px 250px,rgba(190,225,235,.55) 0,rgba(190,225,235,0) 120px),
  radial-gradient(circle at 560px 410px,rgba(170,210,225,.5) 0,rgba(170,210,225,0) 45px),
  radial-gradient(ellipse at 860px 200px,#e8d3c4 0,#d8bfae 140px,rgba(216,191,174,0) 260px),
  linear-gradient(90deg,rgba(29,90,116,0) 40%,rgba(120,170,190,.6) 70%,#9fc3d0 100%)}
.hero-copy{left:78px;top:138px;width:420px;color:var(--white)}
.hero-copy h1{font-family:"Open Sans",sans-serif;font-weight:300;font-size:35px;line-height:1.25}
.hero-copy h2{font-family:"Open Sans",sans-serif;font-weight:600;font-size:19px;margin:10px 0 12px}
.hero-copy p{font-size:14px;line-height:1.75}
.btn{display:inline-block;font-family:"Cinzel",serif;background:var(--navy);color:var(--white);border:6px solid var(--green);border-radius:30px;font-size:21px;padding:8px 28px;letter-spacing:.5px}
.hero-copy .btn{margin-top:22px}

/* welcome */
.welcome{top:677px;height:663px}
.doctor-disc{left:96px;top:135px;width:470px;height:470px;border-radius:50%;background:var(--green-soft)}
.doctor-photo{left:170px;top:68px;width:330px;height:537px;border-radius:160px 160px 0 0;background:linear-gradient(180deg,#d9b79b 0,#ecdccf 22%,#f7f4f1 45%,#ffffff 100%)}
.welcome-copy{left:620px;top:80px;width:470px}
.mini-dot{width:52px;height:52px;border-radius:50%;background:var(--navy);margin-bottom:20px}
.welcome-copy h2{font-family:"Cinzel",serif;font-weight:700;font-size:39px;color:var(--ink);line-height:1;white-space:nowrap}
.kicker{font-family:"Cinzel",serif;color:var(--green);font-size:15px;font-weight:700;margin:8px 0 18px}
.welcome-copy p{font-size:14px;color:var(--grey);line-height:2;margin-bottom:12px}
.welcome-copy .btn{margin-top:14px}

/* services */
.services-band{top:1340px;height:208px;color:var(--white);text-align:center;background:
  radial-gradient(circle at 180px 60px,rgba(255,255,255,.08) 0,rgba(255,255,255,0) 110px),
  radial-gradient(circle at 1000px 140px,rgba(255,255,255,.08) 0,rgba(255,255,255,0) 130px),
  linear-gradient(180deg,#2bb08b,var(--green))}
.services-band h2{font-family:"Cinzel",serif;font-size:43px;padding-top:62px;font-weight:400;letter-spacing:1px}
.services-band .sub{font-family:"Cinzel",serif;font-size:14px;margin-top:6px}
.band-notch{left:562px;top:1546px;width:0;height:0;border-left:38px solid transparent;border-right:38px solid transparent;border-top:36px solid var(--green)}
.service-grid{top:1636px;height:520px}
.service{position:absolute;width:190px;text-align:center}
.service .pic{width:156px;height:156px;border-radius:50%;margin:0 auto 24px}
.service h3{font-family:"Cinzel",serif;font-weight:700;font-size:15px;line-height:1.6;color:var(--ink);padding:0 12px}

/* testimonial */
.testimonial{top:2190px;height:375px;background:
  radial-gradient(ellipse at 640px 200px,rgba(230,240,235,.35) 0,rgba(230,240,235,0) 320px),
  linear-gradient(90deg,#1a9a78,#3cb595 50%,#1a9a78)}
.quote-mark{font-family:"Cinzel",serif;color:var(--white);font-size:190px;line-height:1;font-weight:700}
.testimonial blockquote{left:270px;top:102px;width:660px;text-align:center;color:var(--white);font-style:italic;font-size:18px;line-height:1.85}
.client{left:0;width:1200px;top:240px;text-align:center;font-family:"Cinzel",serif;color:var(--navy);font-size:19px}
.dots{left:0;width:1200px;top:284px;display:flex;justify-content:center;gap:10px}
.dots i{width:14px;height:14px;border-radius:50%;background:rgba(255,255,255,.45)}
.dots i.on{background:var(--white)}

/* contact */
.contact{top:2565px;height:331px;text-align:center}
.contact h2{font-family:"Cinzel",serif;font-weight:700;color:var(--navy);font-size:45px;margin-top:52px}
.contact .intro{width:760px;margin:12px auto 0;font-size:14px;color:var(--grey);line-height:2}
.contact .kicker{margin:14px 0 0}
.contact-items{left:268px;top:218px;display:flex;gap:48px;text-align:left;font-size:14px;color:var(--grey);line-height:1.75}
.contact-items div{display:flex;align-items:center;gap:16px}
.ico{width:56px;height:56px;border-radius:50%;background:var(--green);display:flex;align-items:center;justify-content:center;flex:none}

/* appointment */
.appointment{top:2896px;height:469px}
.map{left:0;top:0;width:1200px;height:469px;background:linear-gradient(135deg,#eceeea,#e2e5e0 60%,#e9ebe7)}
.zoom{right:14px;top:362px;width:26px;background:var(--white);box-shadow:0 1px 3px rgba(0,0,0,.3);font-size:16px;color:#555;text-align:center;line-height:26px}
.zoom span{display:block;border-bottom:1px solid #ddd}
.form-panel{left:91px;top:0;width:396px;height:469px;background:var(--green);padding:34px 34px 0}
.form-panel h2{font-family:"Cinzel",serif;color:var(--white);font-weight:400;font-size:33px;line-height:1.25;margin-bottom:20px}
.field{background:var(--white);height:40px;margin-bottom:8px;font-size:13px;color:var(--grey);padding:10px 14px}
.field.msg{height:96px}
.form-panel .btn{margin:12px 0 0 10px;border-color:var(--green-dark)}

/* footer */
.site-footer{top:3365px;height:64px;background:var(--navy);color:var(--white);font-size:14px;display:flex;align-items:center;padding-left:78px}
.social{right:75px;top:12px;display:flex;gap:10px}
.social i{width:40px;height:40px;border-radius:50%;background:var(--green)}
</style>
</head>
<body>

<header class="site-header">
  <div class="abs topbar">
    <span><svg width="18" height="18" viewBox="0 0 24 24"><path fill="#fff" d="M6.6 10.8a15 15 0 0 0 6.6 6.6l2.2-2.2c.3-.3.7-.4 1-.2 1.1.4 2.3.6 3.6.6.6 0 1 .4 1 1V20c0 .6-.4 1-1 1A17 17 0 0 1 3 4c0-.6.4-1 1-1h3.5c.6 0 1 .4 1 1 0 1.3.2 2.5.6 3.6.1.3 0 .7-.2 1z"/></svg>123 456 7890</span>
    <span><svg width="20" height="16" viewBox="0 0 24 18"><path fill="#fff" d="M0 0h24v18H0z"/><path fill="none" stroke="#1fa27f" stroke-width="2" d="M1 1l11 9 11-9"/></svg>info@varden.example</span>
  </div>
  <div class="abs brand"><span class="brand-dot"></span><span class="brand-name">Varden Institute for Restorative Care</span></div>
  <nav class="abs main-nav">
    <span class="active">HOME</span><span>ABOUT</span><span>SERVICES</span><span>DR.BIO</span><span>TESTIMONILAS</span><span>CONTACT</span>
    <svg width="18" height="18" viewBox="0 0 24 24"><circle cx="10" cy="10" r="7" fill="none" stroke="#0f1c6e" stroke-width="2.5"/><path d="M15 15l7 7" stroke="#0f1c6e" stroke-width="2.5"/></svg>
  </nav>
</header>

<section class="hero">
  <div class="abs hero-photo" role="img" aria-label="Portrait of a woman with short hair beside floating cell spheres"></div>
  <div class="abs hero-copy">
    <h1>Regenerative medicine is the medicine of the future.</h1>
    <h2>It is time that we go back to the origin.</h2>
    <p>Lorem Ipsum is simply dummy text of the printing and type setting industry. Lorem Ipsum has been the industry's standard dummy text ever since the.</p>
    <span class="btn">CONTACT US</span>
  </div>
</section>

<section class="welcome">
  <div class="abs doctor-disc"></div>
  <div class="abs doctor-photo" role="img" aria-label="Doctor in a white coat with a stethoscope, arms crossed"></div>
  <div class="abs welcome-copy">
    <div class="mini-dot"></div>
    <h2>Welcome To Varden</h2>
    <div class="kicker">Institute for Restorative Care</div>
    <p>Lorem Ipsum is simply dummy text of the printing and typesetting industry. Lorem Ipsum has been the industry's standard dummy text ever since the 1500s, when an unknown printer took a galley of type and scrambled it to make a type specimen book. It has survived not only five centuries, but also the leap</p>
    <p>Lorem Ipsum is simply dummy text of the printing and typesetting industry. Lorem Ipsum has been the industry's standard dummy text ever since the 1500s, when an unknown printer took.</p>
    <span class="btn">LEARN MORE</span>
  </div>
</section>

<section class="services-band" role="img" aria-label="Green band with faint cell texture">
  <h2>SERVICE WE PROVIDED</h2>
  <div class="sub">Institute for Restorative Care</div>
</section>
<div class="abs band-notch"></div>

<section class="service-grid">
  <div class="service" style="left:81px;top:0"><div class="pic" role="img" aria-label="Injection being given to a shoulder" style="background:radial-gradient(circle at 65% 55%,#e2b9a0 0,#f1e4dc 55%,#dfe6ec 100%)"></div><h3>NEEDLE-LESS REGENERATIVE INJECTION THERAPY</h3></div>
  <div class="service" style="left:291px;top:0"><div class="pic" role="img" aria-label="Stem cell under a microscope" style="background:radial-gradient(circle,#8f9be0 0,#4a56b8 40%,#27318a 100%)"></div><h3>STEM CELL TREATMENTS</h3></div>
  <div class="service" style="left:504px;top:0"><div class="pic" role="img" aria-label="Woman wrapped in a blanket" style="background:radial-gradient(circle at 45% 40%,#ebc7ae 0,#b8764e 45%,#e9e3dc 80%)"></div><h3>BIOIDENTICAL HORMONE THERAPY</h3></div>
  <div class="service" style="left:716px;top:0"><div class="pic" role="img" aria-label="Colourful pills and a syringe" style="background:radial-gradient(circle at 50% 45%,#e94f7a 0,#f0b44a 25%,#6fc7e0 45%,#f4f4f4 75%)"></div><h3>REATMENT FOR CHRONIC ILLNESS</h3></div>
  <div class="service" style="left:929px;top:0"><div class="pic" role="img" aria-label="Model of a brain" style="background:radial-gradient(circle at 50% 55%,#d45b68 0,#a83a48 35%,#3a3a3a 75%)"></div><h3>NEURODEGENERATIVE DISEASES</h3></div>
  <div class="service" style="left:81px;top:277px"><div class="pic" role="img" aria-label="Woman with skin care markings" style="background:radial-gradient(circle at 45% 45%,#e8d2c3 0,#cdb3a2 45%,#ecebe9 80%)"></div><h3>SKIN REJUVENATION</h3></div>
  <div class="service" style="left:291px;top:277px"><div class="pic" role="img" aria-label="Man with thinning hair" style="background:radial-gradient(circle at 50% 60%,#d5a88d 0,#a07058 45%,#e8e8e8 85%)"></div><h3>HAIR RESTORATION</h3></div>
  <div class="service" style="left:504px;top:277px"><div class="pic" role="img" aria-label="Portrait of a man" style="background:radial-gradient(circle at 50% 50%,#c59a80 0,#6b5245 45%,#2f3640 80%)"></div><h3>MALE ENHANCEMENT</h3></div>
  <div class="service" style="left:716px;top:277px"><div class="pic" role="img" aria-label="Woman in a white top" style="background:radial-gradient(circle at 45% 35%,#e2b48c 0,#d9c2aa 40%,#f6f3f1 75%)"></div><h3>FEMALE ENHANCEMENT</h3></div>
  <div class="service" style="left:929px;top:277px"><div class="pic" role="img" aria-label="Smiling blonde woman" style="background:radial-gradient(circle at 50% 45%,#e9c9a8 0,#cba57c 45%,#6f6f72 85%)"></div><h3>ANTI-AGING</h3></div>
</section>

<section class="testimonial" role="img" aria-label="Green tinted photo of a smiling woman behind a client quote">
  <div class="abs quote-mark" style="left:168px;top:40px">&ldquo;</div>
  <div class="abs quote-mark" style="left:916px;top:150px">&rdquo;</div>
  <blockquote class="abs">Lorem Ipsum is simply dummy text of the printing and typesetting industry. Lorem Ipsum has been the industry's standard dummy text ever since the 1500s, when an unknown printer took.</blockquote>
  <div class="abs client">&mdash; Client Name</div>
  <div class="abs dots"><i></i><i></i><i class="on"></i><i></i><i></i></div>
</section>

<section class="contact">
  <h2>Contact Us</h2>
  <p class="intro">Lorem Ipsum is simply dummy text of the printing and typesetting industry. has been the industry's stand Lorem Ipsum is simply dummy text of the printing and typesetting industry</p>
  <div class="kicker">Schedule Your Appointment</div>
  <div class="abs contact-items">
    <div><span class="ico"><svg width="22" height="28" viewBox="0 0 24 32"><path fill="#fff" d="M12 0A12 12 0 0 0 0 12c0 9 12 20 12 20s12-11 12-20A12 12 0 0 0 12 0zm0 17a5 5 0 1 1 0-10 5 5 0 0 1 0 10z"/></svg></span><span>101 - Lorem ipsum is simple<br>text of print type texty</span></div>
    <div><span class="ico"><svg width="24" height="24" viewBox="0 0 24 24"><path fill="#fff" d="M6.6 10.8a15 15 0 0 0 6.6 6.6l2.2-2.2c.3-.3.7-.4 1-.2 1.1.4 2.3.6 3.6.6.6 0 1 .4 1 1V20c0 .6-.4 1-1 1A17 17 0 0 1 3 4c0-.6.4-1 1-1h3.5c.6 0 1 .4 1 1 0 1.3.2 2.5.6 3.6.1.3 0 .7-.2 1z"/></svg></span><span>123 456 7890</span></div>
    <div><span class="ico"><svg width="24" height="18" viewBox="0 0 24 18"><path fill="#fff" d="M0 0h24v18H0z"/><path fill="none" stroke="#1fa27f" stroke-width="2" d="M1 1l11 9 11-9"/></svg></span><span>info@varden.example</span></div>
  </div>
</section>

<section class="appointment">
  <div class="abs map" role="img" aria-label="Road map of the surrounding area"></div>
  <div class="abs zoom"><span>+</span><span>&minus;</span></div>
  <div class="abs form-panel">
    <h2>Make An<br>Appointment</h2>
    <div class="field">Name *</div>
    <div class="field">Email *</div>
    <div class="field">Phone *</div>
    <div class="field msg">Message *</div>
    <span class="btn">LEARN MORE</span>
  </div>
</section>

<footer class="site-footer">
  ©VARDEN Institute for Restorative Care - 2018 All Right Reserved. Terms of Use
  <div class="abs social" aria-label="Social links"><i></i><i></i><i></i></div>
</footer>

</body>
</html>
```